Need Stunning Website for Talent Acquisition (Recruiting) Agency

Hello, I am seeking a very professional, high-quality website that reflects our Talent Acquisition agency, Kindred Hires. Our agency slogan is "Talent Acquisition. Differently." We are in fact different - we are a full service agency that provides services most others do not, and our website needs to immediately reflect that something is different about us when they visit our site.

This contest is to do complete website design and coding, including all graphics, features, plugins, and design elements. The graphics are very important on the site and must be of the highest professional quality. One critical aspect is that the imagery must convey that we serve clients in a variety of industries, including business, healthcare, churches and religious organizations, non-profits, manufacturing, retail, and more. We recruit for both professional level positions (e.g. CEO, COO, Pastor), as well as entry level (e.g. secretary, caregiver, factory worker).
The following pages should be designed:
Home Page - a captivating home page that immediately tells our brand story, what makes us different, and the value that we bring to the table.
Client Services Page - a page that talks more about the services we provide and why we produce better results. This page will cover the 5 C's in greater detail as well as all the things that make us different.
Industries - The industries we serve
Request Services - a page where clients can submit details about a job they would like us to recruit for, including attaching a job description if they have one
Candidates Page - a simple page that encourages prospective candidates to submit their resume for review
About Us - Common about us page
Blog - Common blog page
Contact Us - a contact page for general inquiries
The website must be built in an ultra-SEO friendly manner and optimized for speed and performance. As mentioned above, you will be responsible for providing all graphics for the site (copyright compliant).
The website will need to be compatible with Elementor Pro (I have subscription) and Yoast SEO. It needs to be designed on a high-quality wordpress theme that receives regular updates. It also needs instant chat messaging feature. Would like a traditional menu bar at the top of the page (not a fan of menu's that are hidden or put on the side of the page).

Please, please, please - - do NOT waste my time with generic/stock templates, low-quality graphics, etc. We are a PREMIUM agency and our website needs to reflect that.

In the future we will add a job board - I do not want that initially - but will want the option to add it later.

Must also have the ability to upload documents /attachments on the contact page/form.

It probably goes without saying, but the page must be fully responsive - suitable to work on all device types.

Target Market(s)

Businesses

Industry/Entity Type

Talent Acquisition (Recruiting) Agency

Coding

Coded - Design and coding required

Number of Pages Required

5+ page

Requirements
Must have
• Please see brief
Should not have
• No generic template/stock website or graphics - must have PREMIUM feel.

```html
<!DOCTYPE html>
<html lang="en">
<head>
<meta charset="utf-8">
<title>Kindred Hires — Talent Acquisition. Differently.</title>
<link href="https://fonts.googleapis.com/css2?family=Poppins:wght@400;500;600;700&display=swap" rel="stylesheet">
<style>
:root{
  --navy:#15184f;
  --orange:#ffa600;
  --cream:#fffaee;
  --text:#3a3d5c;
  --muted:#6b6e85;
  --white:#ffffff;
  --line:#c9cbd8;
}
*{box-sizing:border-box;margin:0;padding:0}
html,body{width:1200px;height:4461px;overflow:hidden}
body{position:relative;font-family:'Poppins',sans-serif;color:var(--text);background:var(--white)}
.abs{position:absolute}
.accent{color:var(--orange)}
.wordmark{font-family:'Poppins',sans-serif;font-weight:600;font-size:26px;line-height:34px;color:var(--navy);display:flex;align-items:center;gap:10px}
.wordmark .mark{width:12px;height:12px;border-radius:50%;background:var(--navy)}
.nav{top:26px;left:395px;display:flex;gap:27px;font-size:13.5px;color:var(--navy)}
.hero-bg{top:0;left:0;width:1200px;height:600px;background:var(--cream)}
.eyebrow{top:148px;left:60px;font-size:15px;color:var(--orange)}
.hero-title{top:176px;left:60px;font-size:39px;line-height:48px;font-weight:600;color:var(--navy)}
.hero-copy{top:284px;left:60px;width:430px;font-size:13.5px;line-height:22.5px;color:var(--muted)}
.btn{display:inline-flex;align-items:center;gap:8px;border-radius:20px;font-size:13px;color:var(--white);padding:0 18px;height:36px}
.btn-navy{background:var(--navy)}
.btn-orange{background:var(--orange)}
.person{border-radius:50%;background:radial-gradient(circle at 50% 40%,#e9d9c8,#b89b84 70%);border:3px solid var(--white);box-shadow:0 3px 10px rgba(0,0,0,.12)}
.person-label{font-size:12px;color:var(--navy);text-align:center;width:140px}
.section-title{left:0;width:1200px;text-align:center;font-size:31px;font-weight:600;color:var(--navy)}
.section-copy{left:0;width:1200px;text-align:center;font-size:13.5px;line-height:22.5px;color:var(--muted)}
.on-navy{color:var(--white)}
.photo{border-radius:22px;overflow:hidden}
.card-title{font-size:25px;font-weight:600;color:var(--orange)}
.card-copy{font-size:13.3px;line-height:22.5px;color:var(--white)}
.industry{text-align:center;font-size:13.5px;font-weight:500;color:var(--navy);width:160px}
.industry .icon{width:70px;height:70px;margin:0 auto 10px;border-radius:50%;background:var(--white);border:2px solid var(--navy);display:flex;align-items:center;justify-content:center}
.testimonial{top:3219px;width:340px;height:212px;background:var(--navy);border-radius:16px;text-align:center;color:var(--white);padding:44px 28px 0}
.testimonial .stars{color:var(--orange);font-size:15px;letter-spacing:2px}
.testimonial .name{color:var(--orange);font-size:14px;margin:2px 0 10px}
.testimonial p{font-size:13.3px;line-height:22.5px}
.avatar{width:64px;height:64px;border-radius:50%;background:radial-gradient(circle at 50% 40%,#efe1d2,#a88a74 70%);border:3px solid var(--white)}
.arrow{width:32px;height:32px;border-radius:50%;display:flex;align-items:center;justify-content:center}
.field{background:var(--white);border:1px solid var(--line);font-size:13px;color:var(--muted);padding:8px 10px;height:33px}
.footer-head{font-size:13.5px;font-weight:500;color:var(--navy)}
.footer-link{font-size:12px;color:var(--muted)}
.social{width:32px;height:32px;border-radius:50%;border:2px solid var(--navy)}
</style>
</head>
<body>

<!-- Hero -->
<div class="abs hero-bg"></div>
<svg class="abs" style="top:520px;left:0" width="1200" height="90" viewBox="0 0 1200 90"><polygon points="0,78 1200,10 1200,0 0,70" fill="var(--cream)"/><line x1="0" y1="80" x2="1200" y2="12" stroke="var(--navy)" stroke-width="3"/></svg>

<div class="abs wordmark" style="top:18px;left:60px"><span class="mark"></span>Kindred Hires</div>
<nav class="abs nav"><span>Home</span><span>Client Services</span><span>Industries</span><span>Request Services</span><span>Candidates</span><span>About Us</span><span>Blog</span><span>Contact Us</span></nav>

<div class="abs eyebrow">Kindred Hires</div>
<h1 class="abs hero-title">Talent Acquisition.<br><span class="accent">Differently.</span></h1>
<p class="abs hero-copy">Lorem Ipsum is simply dummy text of the printing and typesetting industry. Lorem Ipsum has been the industry's standard dummy text ever since the 1500s, when an unknown printer</p>
<a class="abs btn btn-navy" style="top:419px;left:60px">Get Started <svg width="26" height="10" viewBox="0 0 26 10"><path d="M0 5h24M19 1l5 4-5 4" stroke="#fff" fill="none" stroke-width="1.6"/></svg></a>

<svg class="abs" style="top:70px;left:690px" width="480" height="460" viewBox="0 0 480 460">
  <circle cx="238" cy="230" r="180" fill="none" stroke="#f5dba0" stroke-width="1.5"/>
  <circle cx="238" cy="230" r="140" fill="none" stroke="#f5dba0" stroke-width="1.5"/>
  <circle cx="238" cy="230" r="103" fill="var(--white)" stroke="var(--navy)" stroke-width="16"/>
</svg>
<div class="abs person" role="img" aria-label="Portrait of a featured recruiter" style="top:250px;left:880px;width:96px;height:96px"></div>
<div class="abs" style="top:305px;left:953px;width:22px;height:22px;background:var(--orange);transform:rotate(45deg)"></div>
<div class="abs person" role="img" aria-label="Team member portrait" style="top:67px;left:885px;width:80px;height:80px"></div>
<div class="abs person-label" style="top:152px;left:855px">Dana Mercer</div>
<div class="abs person" role="img" aria-label="Team member portrait" style="top:192px;left:1058px;width:80px;height:80px"></div>
<div class="abs person-label" style="top:278px;left:1030px">Dana Mercer</div>
<div class="abs person" role="img" aria-label="Team member portrait" style="top:213px;left:710px;width:80px;height:80px"></div>
<div class="abs person-label" style="top:298px;left:674px">Dana Mercer</div>
<div class="abs person" role="img" aria-label="Team member portrait" style="top:383px;left:1020px;width:80px;height:80px"></div>
<div class="abs person-label" style="top:470px;left:995px">Dana Mercer</div>
<div class="abs person" role="img" aria-label="Team member portrait" style="top:415px;left:800px;width:80px;height:80px"></div>
<div class="abs person-label" style="top:502px;left:765px">Dana Mercer</div>

<!-- Help company -->
<h2 class="abs section-title" style="top:655px">Help Company and <span class="accent">employee to grow</span></h2>
<p class="abs section-copy" style="top:703px">Lorem Ipsum is simply dummy text of the printing and typesetting industry. Lorem Ipsum has<br>been the industry's standard dummy text ever since the 1500s, when an unknown printer</p>

<!-- Navy services band -->
<svg class="abs" style="top:1000px;left:0" width="1200" height="1154" viewBox="0 0 1200 1154"><polygon points="0,0 1200,70 1200,1154 0,1154" fill="var(--navy)"/><polygon points="0,0 1200,70 1200,80 0,8" fill="var(--orange)"/></svg>

<div class="abs photo" role="img" aria-label="Video still: colleagues meeting around a table" style="top:778px;left:272px;width:656px;height:394px;background:linear-gradient(135deg,#4a3b2e,#8a6a4c 50%,#3d3a3a)"></div>
<div class="abs" style="top:957px;left:582px;width:36px;height:36px;border-radius:50%;background:var(--orange);display:flex;align-items:center;justify-content:center"><svg width="14" height="14" viewBox="0 0 14 14"><path d="M3 1l10 6-10 6z" fill="#fff"/></svg></div>

<h2 class="abs section-title on-navy" style="top:1229px">Client Services <span class="accent">We Provides</span></h2>
<p class="abs section-copy" style="top:1275px;color:#d9dbe8">Lorem Ipsum is simply dummy text of the printing and typesetting industry. Lorem Ipsum has<br>been the industry's standard dummy text ever since the 1500s, when an unknown printer</p>

<div class="abs photo" role="img" aria-label="Photo: two businessmen shaking hands in an office" style="top:1358px;left:60px;width:494px;height:332px;background:linear-gradient(135deg,#dfe6ea,#b8c4cc 55%,#2d3340)"></div>
<h3 class="abs card-title" style="top:1392px;left:601px">Talent Acquisition agency</h3>
<p class="abs card-copy" style="top:1438px;left:601px;width:540px">Lorem Ipsum is simply dummy text of the printing and typesetting industry. Lorem Ipsum has been the industry's standard dummy text ever since the 1500s, when an unknown printer took a galley of type and scrambled it to make a type specimen book. It has survived not only five centuries, but also the leap into electronic typesetting, remaining essentially unchanged. It was popularised in the 1960s with the release of Letraset sheets containing</p>

<h3 class="abs card-title" style="top:1810px;left:60px">job they would like us to recruit for</h3>
<p class="abs card-copy" style="top:1858px;left:60px;width:540px">Lorem Ipsum is simply dummy text of the printing and typesetting industry. Lorem Ipsum has been the industry's standard dummy text ever since the 1500s, when an unknown printer took a galley of type and scrambled it to make a type specimen book. It has survived not only five centuries, but also the leap into electronic typesetting, remaining essentially unchanged. It was popularised in the 1960s with the release of Letraset sheets containing</p>
<div class="abs photo" role="img" aria-label="Photo: smiling candidates in a job interview" style="top:1765px;left:644px;width:496px;height:332px;background:linear-gradient(135deg,#e8ecef,#9aa6b3 50%,#2b2e3a)"></div>

<!-- Industries -->
<h2 class="abs section-title" style="top:2228px">The Industries <span class="accent">We Serve</span></h2>
<p class="abs section-copy" style="top:2274px">Lorem Ipsum is simply dummy text of the printing and typesetting industry. Lorem Ipsum has<br>been the industry's standard dummy text ever since the 1500s, when an unknown printer</p>
<svg class="abs" style="top:2360px;left:0" width="1200" height="180" viewBox="0 0 1200 180"><path d="M0 20 C60 50 90 90 144 82 S260 100 331 96 S430 40 514 44 S640 30 710 58 S820 110 888 112 S1010 140 1069 122 S1160 70 1200 40" fill="none" stroke="var(--orange)" stroke-width="1.6"/></svg>

<div class="abs industry" style="top:2407px;left:64px"><div class="icon"><svg width="34" height="34" viewBox="0 0 34 34" fill="none" stroke="var(--navy)" stroke-width="1.6"><rect x="4" y="11" width="26" height="18" rx="2"/><path d="M12 11V7h10v4M4 18h26"/><rect x="15" y="16" width="4" height="5" fill="var(--orange)" stroke="none"/></svg></div>business</div>
<div class="abs industry" style="top:2421px;left:251px"><div class="icon"><svg width="34" height="34" viewBox="0 0 34 34" fill="none" stroke="var(--navy)" stroke-width="1.6"><path d="M17 12c-2-4-8-3-7 2 1 3 7 7 7 7s6-4 7-7c1-5-5-6-7-2z" stroke="var(--orange)"/><path d="M5 14v10l7 5M29 14v10l-7 5"/></svg></div>healthcare</div>
<div class="abs industry" style="top:2369px;left:434px"><div class="icon"><svg width="34" height="34" viewBox="0 0 34 34" fill="none" stroke="var(--navy)" stroke-width="1.6"><path d="M17 3v6M14 6h6" stroke="var(--orange)"/><path d="M9 16l8-7 8 7v13H9zM4 29h26M15 29v-6h4v6"/></svg></div>churches and religious<br>organizations</div>
<div class="abs industry" style="top:2383px;left:630px"><div class="icon"><svg width="34" height="34" viewBox="0 0 34 34" fill="none" stroke="var(--navy)" stroke-width="1.6"><path d="M17 14c-2-4-7-3-6 1 1 3 6 5 6 5s5-2 6-5c1-4-4-5-6-1z" stroke="var(--orange)"/><path d="M3 22h8l6 3h10l4-4M3 28h20l8-5"/></svg></div>non-profits</div>
<div class="abs industry" style="top:2438px;left:808px"><div class="icon"><svg width="34" height="34" viewBox="0 0 34 34" fill="none" stroke="var(--navy)" stroke-width="1.6"><circle cx="17" cy="9" r="4" stroke="var(--orange)"/><path d="M8 16h18M11 16v6M23 16v6M5 24h24v5H5z"/></svg></div>manufacturing</div>
<div class="abs industry" style="top:2448px;left:989px"><div class="icon"><svg width="34" height="34" viewBox="0 0 34 34" fill="none" stroke="var(--navy)" stroke-width="1.6"><path d="M5 8h24l-2 7H7z" stroke="var(--orange)"/><path d="M7 15v14h20V15M13 29v-7h8v7"/></svg></div>retail</div>

<!-- Request services band -->
<svg class="abs" style="top:2595px;left:0" width="1200" height="396" viewBox="0 0 1200 396"><polygon points="0,50 1200,10 1200,396 0,396" fill="var(--orange)"/><line x1="0" y1="48" x2="1200" y2="8" stroke="var(--navy)" stroke-width="3"/></svg>
<div class="abs photo" role="img" aria-label="Photo: person typing at a desktop showing an apply now form" style="top:2608px;left:60px;width:494px;height:332px;background:linear-gradient(135deg,#eef1f3,#c7b49a 55%,#3a3230)"></div>
<h2 class="abs" style="top:2680px;left:613px;font-size:31px;font-weight:600;color:var(--white)">Request Services Kindred Hires</h2>
<p class="abs" style="top:2733px;left:613px;width:520px;font-size:13.3px;line-height:22.5px;color:var(--white)">Lorem Ipsum is simply dummy text of the printing and typesetting industry. Lorem Ipsum has been the industry's standard dummy text ever since the 1500s, when an unknown printer took a galley of type and scrambled it to make a type specimen book. It has survived not only five centuries, but also the leap into electronic typesetting, remaining essentially unchanged.</p>
<a class="abs btn btn-navy" style="top:2880px;left:613px">Submit Details <svg width="26" height="10" viewBox="0 0 26 10"><path d="M0 5h24M19 1l5 4-5 4" stroke="#fff" fill="none" stroke-width="1.6"/></svg></a>

<!-- Testimonials -->
<h2 class="abs section-title" style="top:3069px">What Our <span class="accent">Client Says...</span></h2>
<p class="abs section-copy" style="top:3116px">Lorem Ipsum is simply dummy text of the printing and typesetting industry. Lorem Ipsum has<br>been the industry's standard dummy text ever since the 1500s, when an unknown printer</p>

<div class="abs testimonial" style="left:60px"><div class="stars">★★★★★</div><div class="name">Client Name</div><p>Lorem Ipsum is simply dummy text of the printing and typesetting industry. Lorem Ipsum has been the industry's standard dummy text.</p></div>
<div class="abs testimonial" style="left:430px"><div class="stars">★★★★★</div><div class="name">Client Name</div><p>Lorem Ipsum is simply dummy text of the printing and typesetting industry. Lorem Ipsum has been the industry's standard dummy text.</p></div>
<div class="abs testimonial" style="left:800px"><div class="stars">★★★★★</div><div class="name">Client Name</div><p>Lorem Ipsum is simply dummy text of the printing and typesetting industry. Lorem Ipsum has been the industry's standard dummy text.</p></div>
<div class="abs avatar" role="img" aria-label="Client portrait" style="top:3185px;left:197px"></div>
<div class="abs avatar" role="img" aria-label="Client portrait" style="top:3185px;left:567px"></div>
<div class="abs avatar" role="img" aria-label="Client portrait" style="top:3185px;left:938px"></div>
<div class="abs arrow" style="top:3309px;left:44px;background:#fdefcf"><svg width="10" height="14" viewBox="0 0 10 14"><path d="M8 1L2 7l6 6" stroke="var(--navy)" fill="none" stroke-width="1.8"/></svg></div>
<div class="abs arrow" style="top:3309px;left:1124px;background:var(--orange)"><svg width="10" height="14" viewBox="0 0 10 14"><path d="M2 1l6 6-6 6" stroke="#fff" fill="none" stroke-width="1.8"/></svg></div>

<!-- Contact -->
<svg class="abs" style="top:3545px;left:0" width="1200" height="630" viewBox="0 0 1200 630"><polygon points="0,0 1200,70 1200,630 0,630" fill="var(--navy)"/><polygon points="0,0 1200,70 1200,78 0,6" fill="var(--orange)"/><polygon points="0,0 1200,0 1200,70" fill="var(--white)"/></svg>
<h2 class="abs section-title on-navy" style="top:3646px">Get In <span class="accent">Touch</span></h2>
<p class="abs section-copy" style="top:3692px;color:#d9dbe8">Lorem Ipsum is simply dummy text of the printing and typesetting industry. Lorem Ipsum has<br>been the industry's standard dummy text ever since the 1500s, when an unknown printer</p>
<div class="abs field" style="top:3763px;left:270px;width:323px">First Name*</div>
<div class="abs field" style="top:3763px;left:607px;width:323px">Last Name*</div>
<div class="abs field" style="top:3808px;left:270px;width:323px">E-mail*</div>
<div class="abs field" style="top:3808px;left:607px;width:323px">Phone No*</div>
<div class="abs field" style="top:3853px;left:270px;width:323px">Company Name*</div>
<div class="abs field" style="top:3853px;left:607px;width:323px">Job Title*</div>
<div class="abs field" style="top:3900px;left:270px;width:660px;height:147px">How Can We Help*</div>
<a class="abs btn btn-orange" style="top:4087px;left:543px;height:34px">Submit <svg width="26" height="10" viewBox="0 0 26 10"><path d="M0 5h24M19 1l5 4-5 4" stroke="#fff" fill="none" stroke-width="1.6"/></svg></a>

<!-- Footer -->
<div class="abs wordmark" style="top:4228px;left:60px"><span class="mark"></span>Kindred Hires</div>
<div class="abs social" style="top:4309px;left:60px"></div>
<div class="abs social" style="top:4309px;left:108px"></div>
<div class="abs social" style="top:4309px;left:156px"></div>
<div class="abs social" style="top:4309px;left:204px"></div>
<div class="abs footer-link" style="top:4391px;left:60px">2022© Kindred Hires. All right reserved.</div>

<div class="abs footer-head" style="top:4237px;left:497px">Company</div>
<div class="abs footer-link" style="top:4270px;left:500px">Home</div>
<div class="abs footer-link" style="top:4300px;left:500px">Client Services</div>
<div class="abs footer-link" style="top:4330px;left:500px">Industries</div>
<div class="abs footer-link" style="top:4360px;left:500px">Request Services</div>
<div class="abs footer-link" style="top:4391px;left:500px">Candidates</div>
<div class="abs footer-link" style="top:4270px;left:637px">About Us</div>
<div class="abs footer-link" style="top:4300px;left:637px">Blog</div>
<div class="abs footer-link" style="top:4330px;left:637px">Contact Us</div>

<div class="abs footer-head" style="top:4237px;left:947px">Legal</div>
<div class="abs footer-link" style="top:4270px;left:947px">Terms &amp; Condition</div>
<div class="abs footer-link" style="top:4300px;left:947px">Privecy Policy</div>

<div class="abs" style="top:4366px;left:1100px;width:38px;height:38px;border-radius:50%;background:var(--orange);display:flex;align-items:center;justify-content:center"><svg width="20" height="18" viewBox="0 0 20 18"><path d="M2 2h12v8H7l-4 3v-3H2z" fill="var(--navy)"/><path d="M8 12h6l3 3v-3h1V5h-2" fill="none" stroke="var(--navy)" stroke-width="1.5"/></svg></div>

</body>
</html>
```